Mesa Copperline Distributors Sales Training

I need a job posting flyer for a hands on Sales Training positions in the electrical distribution market of Phoenix, Arizona. The flyer will be posted on college campuses to recruit new grads for my company. I would like to highlight the benefits of Professional Sales jobs such as a flexible schedule, some out of state travel for training, accelerating career path, and control of earnings based on performance. This is not an everyday sales position, it is professional, complex, and competitive. Applicants should have an entrepreneurial mindset as they will run their accounts as their own business. Mesa Copperline Distributors sells construction electric material to customers in a large scale including electrical conduit, Wire, fittings, high tech lighting and building controls along with other green energy saving devices.
Applicants will send resumes to DaleR@MCDsonoran.com

I have added some pictures that inspire me

Target Market(s)

New college graduates, any bachelors degree

Industry/Entity Type

Electrical Equipment

Font styles to use
Serif

Colors

Designer to choose colors to be used in the design.

Requirements
Must have
• Photos that help show what our industry does, most people are unaware of this industry
• Not wordy, short, get the point across, and where to apply
Nice to have
• creativity and simplicity
Should not have
• too many words

```html
<!DOCTYPE html>
<html lang="en">
<head>
<meta charset="utf-8">
<title>Mesa Copperline Distributors – Sales Training Recruit</title>
<link rel="stylesheet" href="https://fonts.googleapis.com/css2?family=Oswald:wght@500&family=Pacifico&family=PT+Sans:ital,wght@0,400;0,700;1,700&family=PT+Serif:wght@700&display=swap">
<style>
  :root {
    --ink: #1a1a1a;
    --black: #000000;
    --red: #ee2a35;
    --grey: #d1d2d4;
    --white: #ffffff;
    --text-dark: #3a3a3a;
  }
  * { margin: 0; padding: 0; box-sizing: border-box; }
  html, body { width: 887px; height: 1200px; overflow: hidden; background: var(--white); }
  .flyer { position: relative; width: 887px; height: 1200px; background: var(--white); font-family: "PT Sans", sans-serif; }

  .frame-top { position: absolute; left: 0; top: 0; width: 887px; height: 553px; background: var(--black); }
  .panel { position: absolute; left: 43px; top: 91px; width: 805px; height: 526px; background: var(--white); }

  .headline {
    position: absolute; left: 83px; top: 150px;
    font-family: "Oswald", sans-serif; font-weight: 500; font-size: 33px;
    letter-spacing: -0.5px; color: var(--text-dark); transform: scaleX(0.82); transform-origin: left;
  }
  .headline .accent { font-family: "Pacifico", cursive; color: var(--red); font-size: 26px; margin-left: 6px; }

  .brand {
    position: absolute; left: 470px; top: 146px; width: 355px;
    display: flex; align-items: center; gap: 10px;
    font-family: "PT Sans", sans-serif; font-weight: 700; font-size: 21px; color: var(--ink);
  }
  .brand-mark { width: 18px; height: 18px; background: var(--red); flex: none; }

  .photo {
    position: absolute; left: 156px; top: 199px; width: 595px; height: 418px;
    background: linear-gradient(90deg, #4a5470 0%, #c9333c 30%, #d9cfc7 50%, #e96f4a 65%, #f2c428 85%, #d8354a 100%);
    border-radius: 140px 140px 0 0;
  }

  .title-band {
    position: absolute; left: 43px; top: 617px; width: 805px; height: 127px; background: var(--red);
    display: flex; align-items: center; justify-content: center;
  }
  .title-band h1 {
    font-family: "Pacifico", cursive; font-weight: 400; font-size: 56px; color: var(--white);
    text-shadow: 2px 3px 4px rgba(0,0,0,0.35); letter-spacing: -1px;
  }

  .sub-band {
    position: absolute; left: 43px; top: 744px; width: 805px; height: 93px; background: var(--grey);
    display: flex; align-items: center; justify-content: center; text-align: center;
  }
  .sub-band p { font-weight: 700; font-size: 31px; line-height: 42px; color: var(--ink); letter-spacing: -0.3px; }

  .info-band { position: absolute; left: 43px; top: 837px; width: 805px; height: 213px; background: var(--red); color: var(--white); }
  .about {
    position: absolute; left: 19px; top: 20px; width: 385px;
    font-size: 17.5px; line-height: 27.6px; text-align: justify;
  }
  .about strong { font-weight: 700; }
  .divider { position: absolute; left: 434px; top: 22px; width: 1px; height: 175px; background: rgba(0,0,0,0.25); }
  .benefits { position: absolute; left: 469px; top: 18px; }
  .benefits h2 { font-family: "PT Serif", serif; font-weight: 700; font-size: 29px; margin-bottom: 12px; }
  .benefits ul { list-style: none; }
  .benefits li { position: relative; padding-left: 24px; font-weight: 700; font-size: 17px; line-height: 25px; width: 320px; }
  .benefits li::before {
    content: ""; position: absolute; left: 0; top: 9px; width: 12px; height: 12px; border-radius: 50%; background: var(--black);
  }

  .apply {
    position: absolute; left: 58px; top: 1064px; width: 776px; height: 55px;
    border-bottom: 1px solid #c8c8c8; color: var(--text-dark); white-space: nowrap;
  }
  .apply em { font-style: italic; font-weight: 700; font-size: 25px; }
  .apply .email { font-weight: 700; font-size: 34px; margin-left: 4px; }
  .website {
    position: absolute; left: 0; top: 1126px; width: 887px; text-align: center;
    font-weight: 700; font-size: 31px; letter-spacing: 2px; color: var(--red);
  }
</style>
</head>
<body>
<main class="flyer">
  <div class="frame-top"></div>
  <div class="panel"></div>

  <p class="headline">PROFESSIONAL SALES JOBS<span class="accent">in</span></p>
  <div class="brand"><span class="brand-mark"></span>Mesa Copperline Distributors</div>

  <div class="photo" role="img" aria-label="Photo of four smiling young college graduates holding folders and notebooks"></div>

  <section class="title-band"><h1>Sales Training Recruit</h1></section>

  <section class="sub-band">
    <p>Sales Training positions in the electrical<br>distribution market of Phoenix, Arizona</p>
  </section>

  <section class="info-band">
    <p class="about"><strong>Mesa Copperline Distributors sells:</strong> Construction Electric Material to customers in a large scale including Electrical Conduit, Wire, Fittings, High Tech Lighting and Building Controls along with other Green Energy Saving Devices.</p>
    <div class="divider"></div>
    <div class="benefits">
      <h2>Benefits:</h2>
      <ul>
        <li>Flexible schedule</li>
        <li>Some out of state travel for training</li>
        <li>Accelerating career path</li>
        <li>Control of earnings based on performance</li>
      </ul>
    </div>
  </section>

  <p class="apply"><em>Applicants will send resumes to</em><span class="email">DaleR@MCDsonoran.com</span></p>
  <p class="website">www.MCDsonoran.partsdesk.com</p>
</main>
</body>
</html>
```